Wine Label Design

A wine label for 750ml bottles. Same label for different varieties with the variety / region / vintage to be updated as required.
Brand: Beyond the Ridge
Product Use: Front and Back label suitable for a 750 ml bottle (preferably Burgundy bottles)
Design Brief: Beyond the Ridge is a small winery that produces limited amounts of hand crafted wines that are aimed at the mid to top end of the market and requires a label befitting the work that goes into the creation of the wine. In terms of style i don't have any preconceptions and am open to a broad range of design suggestions at the same level of existing premium brands or innovative brands.
Must Have for Front label
Front Label
Beyond the Ridge
2013
Grampians
Shiraz
750ML (should be in smaller text)
Alc. 14% by Vol. (should be in smaller text)
Must Have for Back Label
Beyond the Ridge
2013
Grampians
Shiraz
www.beyondtheridge.com.au (should be in smaller text)
Product of Australia
Alc.14% by Vol. (should be in smaller text)
Contains preservative 220(should be in smaller text)
Below are some guides for dimensions:
The Front Label Size can be between
100 - 120 mm (Width) x 70 - 85 mm (Height)
The back label size can be between
90 mm (Width) x 70 - 85 mm (Height)
Updates
Target Market(s)
Medium to top end of the wine market who require the label to be a reflection of the wine.
Industry/Entity Type
Product
Colors
Designer to choose colors to be used in the design.
Look and feel
Each slider illustrates characteristics of the customer's brand and the style your logo design should communicate.

```html
<!DOCTYPE html>
<html lang="en">
<head>
<meta charset="utf-8">
<title>Beyond the Ridge – Grampians Shiraz 2013 Front Label</title>
<link href="https://fonts.googleapis.com/css2?family=Source+Sans+3:wght@400&display=swap" rel="stylesheet">
<style>
  :root {
    --label-charcoal: #373635;
    --label-white: #ffffff;
    --tone-orange: #e87621;
    --tone-green: #006a3e;
    --tone-plum: #8b547a;
    --tone-olive: #6a8f2f;
  }
  html, body {
    margin: 0;
    padding: 0;
    overflow: hidden;
    background: var(--label-charcoal);
  }
  .label {
    position: relative;
    width: 1163px;
    height: 1200px;
    overflow: hidden;
    background: var(--label-charcoal);
    font-family: "Source Sans 3", "Myriad Pro", sans-serif;
    color: var(--label-white);
  }
  .label__heading {
    position: absolute;
    left: 342px;
    top: 0;
    margin: 0;
  }
  .label__brand {
    position: absolute;
    top: 80px;
    left: 0;
    margin: 0;
    font-size: 58px;
    font-weight: 400;
    letter-spacing: -0.5px;
    line-height: 1;
    white-space: nowrap;
    text-transform: uppercase;
  }
  .label__region,
  .label__variety,
  .label__vintage {
    position: absolute;
    left: 0;
    margin: 0;
    font-size: 40px;
    font-weight: 400;
    line-height: 1;
    white-space: nowrap;
  }
  .label__region { top: 196px; }
  .label__variety { top: 254px; }
  .label__vintage { top: 356px; }
  .label__landscape {
    position: absolute;
    left: 276px;
    top: 477px;
    right: 0;
    bottom: 0;
    background: linear-gradient(
      to bottom,
      var(--tone-orange) 0%,
      var(--tone-green) 35%,
      var(--tone-plum) 62%,
      var(--tone-olive) 100%
    );
  }
  .label__legal {
    position: absolute;
    left: 30px;
    bottom: 31px;
    display: flex;
    flex-direction: row;
    gap: 6px;
  }
  .label__legal-line {
    margin: 0;
    writing-mode: vertical-rl;
    transform: rotate(180deg);
    font-size: 22px;
    line-height: 1;
    white-space: nowrap;
  }
</style>
</head>
<body>
<main class="label">
  <header class="label__heading">
    <h1 class="label__brand">Beyond the Ridge</h1>
    <p class="label__region">Grampians</p>
    <p class="label__variety">Shiraz</p>
    <p class="label__vintage">2013</p>
  </header>
  <div class="label__landscape" role="img" aria-label="Stylised landscape of layered rolling hills in orange, green, plum and olive"></div>
  <div class="label__legal">
    <p class="label__legal-line">750ML</p>
    <p class="label__legal-line">Alc. 14% by Vol.</p>
  </div>
</main>
</body>
</html>
```